Wealth management firm needs a business card design

Using my logo, create a business card that covers all of the regulatory wordings that I need. It must have - Registered Office 7-9 Pelgrove Wynd, Edinburgh, EH4 2QN. Registered in Scotland under number SC804317. VORELT Wealth Management Ltd is an appointed representative of Kestoby wealth management Ltd, which is authorised and regulated by the Monetary Oversight Council.

Target Market(s)

professional clients

Industry/Entity Type

finance

Contact Information for Business Card

VORELT Wealth Management, Conor Tresk-Whitlaw, Director, 5 Dunmore Row, Edinburgh, EH9 4RT. 07812 459 163, conor.tresk-whitlaw@vorelt-example.com , www.vorelt-example.com

Font styles to use
Serif

Colors
0054AA
0677BA
7BADD7
CADEEF
E8F1F8

Requirements
Must have
• regulatory wording in small text at bottom

```html
<!DOCTYPE html>
<html lang="en">
<head>
<meta charset="utf-8">
<title>VORELT Wealth Management – Business Card</title>
<link rel="stylesheet" href="https://fonts.googleapis.com/css2?family=Noto+Serif:wght@400;700&display=swap">
<style>
  :root {
    --page-bg: #222222;
    --card-bg: #282a33;
    --card-edge: #3d78c4;
    --accent-blue: #3d78c4;
    --text-light: #f2f2f2;
    --text-muted: #d8d8dc;
    --text-fine: #9a9ca6;
    --emboss-ink: #1a1b21;
    --deco-light: #5a5b60;
    --deco-dark: #141418;
  }
  * { margin: 0; padding: 0; box-sizing: border-box; }
  html, body {
    width: 1200px; height: 780px; overflow: hidden;
    background: var(--page-bg);
    font-family: "Noto Serif", Georgia, serif;
  }
  .sheet {
    position: relative; width: 1200px; height: 780px;
    display: flex; align-items: center; justify-content: center; gap: 40px;
  }
  .card {
    position: relative; width: 540px; height: 340px;
    background: var(--card-bg);
    border-radius: 22px;
    border-bottom: 3px solid var(--card-edge);
    border-left: 3px solid var(--card-edge);
    overflow: hidden;
  }

  /* Back of card */
  .card-back .brand {
    position: absolute; left: 0; right: 0; top: 96px;
    display: flex; flex-direction: column; align-items: center; gap: 12px;
  }
  .card-back .brand-dot {
    width: 62px; height: 62px; border-radius: 50%;
    background: var(--emboss-ink);
  }
  .card-back .brand-name {
    font-size: 27px; font-weight: 700; color: var(--emboss-ink);
    white-space: nowrap;
  }
  .card-back .brand-tagline {
    font-size: 12px; color: var(--emboss-ink);
    margin-top: -8px; padding-left: 120px;
  }

  /* Front of card */
  .card-front .holder {
    position: absolute; right: 34px; top: 22px; text-align: right;
  }
  .card-front .holder-name {
    font-size: 21px; font-weight: 700; color: var(--accent-blue);
    white-space: nowrap;
  }
  .card-front .holder-role {
    font-size: 11px; color: var(--text-light); margin-top: 2px;
  }
  .card-front .edge-tab {
    position: absolute; right: 0; top: 20px; width: 16px; height: 46px;
    background: var(--accent-blue);
  }
  .card-front .brand {
    position: absolute; left: 34px; top: 74px;
  }
  .card-front .brand-dot {
    display: block; width: 34px; height: 34px; border-radius: 50%;
    background: var(--accent-blue); margin: 0 0 8px 70px;
  }
  .card-front .brand-name {
    font-size: 17px; font-weight: 400; color: var(--text-light);
    white-space: nowrap;
  }
  .card-front .brand-tagline {
    font-size: 8px; color: var(--text-light);
    padding-left: 130px; margin-top: 1px;
  }
  .card-front .pattern-area {
    position: absolute; left: 336px; top: 84px; width: 184px; height: 196px;
    border-radius: 50%;
    background: radial-gradient(ellipse at 50% 20%, var(--deco-light) 0%, var(--deco-dark) 75%, transparent 76%);
    opacity: 0.85;
  }
  .card-front .address {
    position: absolute; left: 52px; top: 174px;
    font-size: 12px; line-height: 1.35; color: var(--text-muted); font-style: normal;
  }
  .card-front .contacts {
    position: absolute; left: 52px; top: 214px;
    list-style: none; font-size: 12px; color: var(--text-muted);
  }
  .card-front .contacts li {
    display: flex; align-items: center; gap: 8px; height: 20px; white-space: nowrap;
  }
  .card-front .contacts svg { width: 12px; height: 12px; flex: none; }
  .card-front .regulatory {
    position: absolute; left: 34px; right: 34px; bottom: 10px;
    font-size: 7px; line-height: 1.4; color: var(--text-fine); text-align: center;
  }
</style>
</head>
<body>
<main class="sheet">

  <section class="card card-back" aria-label="Business card back">
    <div class="brand">
      <span class="brand-dot" aria-hidden="true"></span>
      <span class="brand-name">VORELT Wealth Management Ltd</span>
      <span class="brand-tagline">Personal Financial Advice</span>
    </div>
  </section>

  <section class="card card-front" aria-label="Business card front">
    <div class="edge-tab" aria-hidden="true"></div>
    <div class="holder">
      <div class="holder-name">Conor Tresk-Whitlaw</div>
      <div class="holder-role">Director</div>
    </div>

    <div class="brand">
      <span class="brand-dot" aria-hidden="true"></span>
      <div class="brand-name">VORELT Wealth Management Ltd</div>
      <div class="brand-tagline">Personal Financial Advice</div>
    </div>

    <div class="pattern-area" role="img" aria-label="Decorative area of large shaded dots"></div>

    <address class="address">
      5 Dunmore Row, Edinburgh,<br>EH9 4RT.
    </address>

    <ul class="contacts">
      <li>
        <svg viewBox="0 0 24 24" fill="var(--accent-blue)" aria-hidden="true"><path d="M6.6 10.8a15.1 15.1 0 0 0 6.6 6.6l2.2-2.2a1 1 0 0 1 1-.25 11.4 11.4 0 0 0 3.6.57 1 1 0 0 1 1 1V20a1 1 0 0 1-1 1A17 17 0 0 1 3 4a1 1 0 0 1 1-1h3.5a1 1 0 0 1 1 1c0 1.25.2 2.45.57 3.57a1 1 0 0 1-.25 1z"/></svg>
        07812 459 163
      </li>
      <li>
        <svg viewBox="0 0 24 24" fill="none" stroke="var(--accent-blue)" stroke-width="2.4" aria-hidden="true"><circle cx="12" cy="12" r="9.5"/><path d="M2.5 12h19M12 2.5c3 3 3 16 0 19M12 2.5c-3 3-3 16 0 19"/></svg>
        www.vorelt-example.com
      </li>
      <li>
        <svg viewBox="0 0 24 24" fill="none" stroke="var(--accent-blue)" stroke-width="2.4" aria-hidden="true"><rect x="2.5" y="5" width="19" height="14" rx="1.5"/><path d="M3 6l9 7 9-7"/></svg>
        conor.tresk-whitlaw@vorelt-example.com
      </li>
    </ul>

    <p class="regulatory">
      Registered Office 7-9 Pelgrove Wynd, Edinburgh, EH4 2QN. Registered in Scotland under number SC804317.
      VORELT Wealth Management Ltd is an appointed representative of Kestoby wealth management Ltd,
      which is authorised and regulated by the Monetary Oversight Council.
    </p>
  </section>

</main>
</body>
</html>
```